演奏会のメイン曲は、ベネディクト・ハウエル作曲「ラ・フォンテ・ヴェルデ」です。
演奏会全体としては、”希望の光”をイメージしています。
依然コロナ禍にありますが、音楽が”希望の光”になれば…
また、西海沿岸大洪水から10年で、復興支援のために作られた曲も演奏を予定しています。
・団体名
・演奏会名:ハーモニーフェスタ2021
・指揮者名:柳沼俊哉
・場所
・日時:2021年12月12日(日)
・曲目:ラ・フォンテ・ヴェルデ、星は今も瞬く、マルコの幻想の朝、夢にさそわれて…他
・問い合わせ先:担当/水野 090-2716-4098、https://sakuragi-brass.hoshizora-web.com/
など
※場所、チケット情報などは、添付画像と変化なしです。ご覧いただければと思います。
A4
片面
過去のチラシデータを添付いたしますので、ご参照ください。
チラシのデザインが決まれば、チラシのデザインを基に、チケット・ポスター・パンフレットの表紙も追加(1万程度)で作成していただきたいと考えております。
よろしくお願いします。
たくさんのご提案、ありがとうございます。
どれも素敵なデザインで、迷ってしまうという嬉しい悩みです。
わたし個人では決められないため、団体内で相談しようと思います。
相談できる日がお盆明けになる関係で、締め切りを延長しました。
引き続きよろしくお願いいたします。

クリスマスが近い時期の演奏会、という雰囲気に心惹かれました。
また、おしゃれさや見やすさ、演奏会全体の「希望に満ちたイメージ」との相性も含め、こちらのデザインに決めさせていただきました。

すてきなデザインをたくさんご応募いただき、本当にありがとうございました。
他のデザインにも、とても心惹かれました。
またよろしくお願いいたします。

```html
<!DOCTYPE html>
<html lang="ja">
<head>
<meta charset="UTF-8">
<title>ハーモニーフェスタ2021</title>
<link rel="stylesheet" href="https://fonts.googleapis.com/css2?family=Dela+Gothic+One&family=M+PLUS+1p:wght@400;700;800&display=swap">
<style>
:root{
  --cream:#fbf1c8;
  --yellow:#f6d02f;
  --red:#e4322b;
  --navy:#2b2f6b;
  --violet:#6d5fb0;
  --ink:#1b1b1b;
}
*{margin:0;padding:0;box-sizing:border-box}
html,body{width:851px;height:1200px;overflow:hidden}
body{font-family:"M PLUS 1p",sans-serif;color:var(--ink)}
.flyer{position:relative;width:851px;height:1200px;background:var(--cream);overflow:hidden}
.deco{position:absolute;inset:0}
.art-strings{position:absolute;left:560px;top:90px;width:291px;height:470px;border-radius:150px 0 0 150px;
  background:linear-gradient(160deg,#f28a3a 0%,var(--red) 55%,#b9262a 100%);opacity:.9}
.art-winds{position:absolute;left:470px;top:470px;width:381px;height:660px;border-radius:190px 0 0 40px;
  background:linear-gradient(200deg,#4a4f96 0%,var(--navy) 60%,#1f2250 100%)}
.art-brass{position:absolute;left:0;top:1000px;width:260px;height:130px;border-radius:0 70px 70px 0;
  background:linear-gradient(90deg,#e9b94a,#f6d86a)}
.title{position:absolute;left:150px;top:30px;font-family:"Dela Gothic One",sans-serif;line-height:1.05;font-size:96px;letter-spacing:-2px}
.title .year{display:block;color:var(--red);font-size:72px;margin-left:270px;margin-top:10px;letter-spacing:2px}
.date{position:absolute;left:140px;top:300px;font-family:"Dela Gothic One",sans-serif;color:var(--red);display:flex;align-items:flex-end;gap:10px}
.date .y{font-size:36px;line-height:1;padding-bottom:14px}
.date .md{font-size:96px;line-height:.9}
.date .dow{font-family:"M PLUS 1p",sans-serif;font-weight:800;font-size:22px;background:var(--red);color:#fff;border-radius:6px;padding:2px 8px;margin-bottom:14px}
.time{position:absolute;left:150px;top:392px;font-size:22px;font-weight:700}
.time b{color:var(--red);font-size:24px}
.time small{font-size:15px;font-weight:400}
.venue{position:absolute;left:150px;top:425px;font-size:30px;font-weight:800}
.tag{display:inline-block;background:var(--red);color:#fff;font-size:20px;font-weight:800;padding:2px 10px;border-radius:4px;margin-right:14px;vertical-align:middle}
.conductor{position:absolute;left:240px;top:490px;font-size:36px;font-weight:800}
.program{position:absolute;left:240px;top:540px;font-size:29px;font-weight:800;line-height:1.35}
.program ul{list-style:none;margin-top:6px;margin-left:4px}
.ticket{position:absolute;left:50px;top:760px;width:380px}
.ticket h3{font-size:20px;font-weight:800}
.ticket h3 span{font-size:15px;font-weight:700}
.price{font-family:"Dela Gothic One",sans-serif;font-size:56px;color:var(--red);line-height:1.1}
.note{font-size:12px;line-height:1.5;margin-top:4px}
.contact{position:absolute;left:50px;top:965px}
.contact .lbl{font-size:16px;font-weight:800;background:var(--ink);color:#fff;padding:1px 8px;border-radius:3px}
.phone{display:flex;align-items:center;gap:6px;font-family:"Dela Gothic One",sans-serif;font-size:38px;line-height:1.2}
.url{font-size:15px;font-weight:700}
.access{position:absolute;left:50px;top:1075px;font-size:13px;line-height:1.6;z-index:2}
.access .lbl{font-weight:800;border:1px solid var(--ink);padding:0 5px}
.footer{position:absolute;left:0;right:0;bottom:0;height:48px;background:var(--yellow);font-size:12px;display:flex;align-items:center;justify-content:center;padding:0 20px}
</style>
</head>
<body>
<div class="flyer">
  <svg class="deco" width="851" height="1200" viewBox="0 0 851 1200" aria-hidden="true">
    <path d="M0 0 H130 Q60 120 0 170 Z" fill="var(--violet)"/>
    <circle cx="90" cy="560" r="150" fill="var(--yellow)"/>
    <path d="M0 650 Q200 720 420 640 Q440 760 300 820 Q120 880 0 840 Z" fill="#f8de6f"/>
    <path d="M851 0 H700 Q760 60 851 60 Z" fill="var(--yellow)"/>
  </svg>
  <div class="art-strings" role="img" aria-label="赤いギターと弦楽器のイラスト"></div>
  <div class="art-winds" role="img" aria-label="紺色のサクソフォンと音符のイラスト"></div>
  <div class="art-brass" role="img" aria-label="金色のトランペットのイラスト"></div>

  <h1 class="title">ハーモニー<br>フェスタ<span class="year">2021</span></h1>

  <div class="date"><span class="y">2021</span><span class="md">12.12</span><span class="dow">sun</span></div>
  <p class="time"><b>開場</b> 13:00 <b>開演</b> 14:00 <small>(終演16:00)</small></p>
  <p class="venue">桜木市文化会館大ホール</p>

  <p class="conductor"><span class="tag">指揮</span>柳沼 俊哉</p>
  <div class="program"><span class="tag">曲目</span>
    <ul>
      <li>ラ・フォンテ・ヴェルデ、</li>
      <li>星は今も瞬く、</li>
      <li>マルコの幻想の朝、</li>
      <li>夢にさそわれて…他</li>
    </ul>
  </div>

  <div class="ticket">
    <h3>Ticket <span>【前売り券/当日券】</span></h3>
    <p class="price">¥500</p>
    <p class="note">未就学児のご入場はご遠慮ください。<br>チケット取扱い：ハルモニア楽器店・桜木市文化会館ほか</p>
  </div>

  <div class="contact">
    <span class="lbl">問い合わせ先</span> <b>担当/水野</b>
    <p class="phone">
      <svg width="30" height="30" viewBox="0 0 24 24" aria-hidden="true"><path fill="var(--ink)" d="M6.6 10.8a15 15 0 0 0 6.6 6.6l2.2-2.2a1 1 0 0 1 1-.25 11.4 11.4 0 0 0 3.6.57 1 1 0 0 1 1 1V20a1 1 0 0 1-1 1A17 17 0 0 1 3 4a1 1 0 0 1 1-1h3.5a1 1 0 0 1 1 1c0 1.25.2 2.45.57 3.57a1 1 0 0 1-.25 1z"/></svg>
      090-2716-4098</p>
    <p class="url">https://sakuragi-brass.hoshizora-web.com/</p>
  </div>

  <div class="access">
    <span class="lbl">アクセス</span><br>
    桜木県桜木市若葉町1丁目30番地<br>
    ● 桜木中央駅下車徒歩20分<br>
    ● わかば循環バス「文化会館」下車
  </div>

  <p class="footer">(主催)桜木市吹奏楽団 (後援)桜木市・桜木市教育委員会・みなと新聞社・桜木市文化協会</p>
</div>
</body>
</html>
```